Pinecrest Treatment Brochure for a drug and alcohol addiction treatment center.

***Update #2***
For graphic highlights no intrusion into text and no fade into adjoining areas.Use modern clean white layout with grey and light orange color scheme. Use attached yoga photo and other photos. For cover try moving number and logo around, and also try with cover photo not full size. Also use larger text with bullet points in a couple spots. Also try with new attached cover photos.
***Update*** I have attached some new photos to clarify the design wanted. My client likes the size (but not design) of the brochure in the newly included photos. Note the measurements - when closed it is 6" wide x 7" tall. When fully open it is 18" long, 7" wide, with 2 folds. I apologize if my terminology below was confusing. Please confirm that your design reflects the desired layout, and please modify your design if it does not. Thanks!
Want a trifold brochure 6" wide x 7" height. Design is for a drug and alcohol addiction treatment center. We want clean, soft, contemporary with highlight colors orange and grey, with contemporary font. Maybe some soft curves on design - see this A4 design we like but not the colors:
http://stockmosaic.example/item/corporate-folded-leaflet-ripple/7391052?s_phrase=trifold%20business%20brochure&s_rank=54
See company web site for style cues and some content you can use:
http://pinecrestcarehub.example/
You can use the attached photos and logo in the design. Try sun in hand photo on cover, or man on beach. Please do not use the words "The Pinecrest Treatment Center" in verbiage or titles, for business reasons we want to use "Pinecrest Treatment Center" with no "The" instead.
Please note that the logo has been updated. The new logo is attached below. Use pinecrest rev2.png for logo.
Addiction treatment industry professionals; family and decision makers of addict; addict themselves.
Health And Wellness

```html
<!DOCTYPE html>
<html lang="en">
<head>
<meta charset="utf-8">
<title>Pinecrest Treatment Center – Trifold Brochure</title>
<link href="https://fonts.googleapis.com/css2?family=Montserrat:wght@300;400;500;600&display=swap" rel="stylesheet">
<style>
  :root{
    --bg:#b0afad;
    --paper:#ffffff;
    --orange:#f07a1f;
    --amber:#f5b21a;
    --grey:#bdbdbd;
    --grey-band:#e3e3e3;
    --ink:#1e1e1e;
    --body:#3a3a3a;
    --soft:#6f6f6f;
  }
  *{margin:0;padding:0;box-sizing:border-box}
  html,body{width:1200px;height:945px;overflow:hidden;background:var(--bg);font-family:"Montserrat",sans-serif}
  .spread{position:absolute;left:30px;top:251px;width:1140px;height:443px;background:var(--paper);box-shadow:0 6px 18px rgba(0,0,0,.18);overflow:hidden}
  .waves{position:absolute;left:0;top:0;width:1140px;height:443px}
  .panel{position:absolute;top:0;width:380px;height:443px}
  .panel--about{left:0}
  .panel--services{left:380px;border-left:1px solid #eeeeee}
  .panel--drug{left:760px;border-left:1px solid #eeeeee}
  .section-title{position:absolute;font-weight:300;font-size:26px;color:var(--orange);letter-spacing:-.3px}
  .section-title svg{position:absolute;left:-22px;top:2px;width:140px;height:50px;overflow:visible}
  .intro{position:absolute;left:24px;top:94px;width:330px;font-size:10.5px;line-height:1.45;font-weight:300;color:var(--soft)}
  .photo{position:absolute;border-radius:14px}
  .photo--yoga{left:22px;top:172px;width:150px;height:200px;background:linear-gradient(180deg,#b98fb0 0%,#f3a35c 45%,#f6c98a 60%,#8d6c90 100%)}
  .photo--group{left:20px;top:120px;width:128px;height:168px;background:linear-gradient(160deg,#e9e9e9 0%,#cfc6bd 55%,#5b5250 100%)}
  .photo--talk{left:18px;top:120px;width:135px;height:178px;background:linear-gradient(150deg,#e7e2dc 0%,#c4b6a8 50%,#6f7d8c 100%)}
  .photo--room{right:0;top:0;width:220px;height:105px;border-radius:0;background:linear-gradient(200deg,#7f8c6a 0%,#b99c73 45%,rgba(255,255,255,0) 100%)}
  .side-text{position:absolute;font-size:7.2px;line-height:1.5;color:var(--body)}
  .side-text--tight{line-height:1.4}
  .side-text p+p{margin-top:8px}
  .sub-title{position:absolute;font-weight:500;font-size:16px;color:var(--ink)}
  .brand{position:absolute;left:200px;top:410px;display:flex;align-items:center;gap:6px;font-weight:600;font-size:11px;color:var(--orange);text-transform:uppercase}
  .brand-dot{width:16px;height:16px;border-radius:50%;background:var(--orange)}
  .call{position:absolute;left:0;width:380px;top:410px;text-align:center;font-size:14px;color:var(--ink)}
  .call strong{color:var(--orange);font-weight:500}
  .site{position:absolute;right:40px;top:414px;font-size:11px;font-weight:600;color:#fff;letter-spacing:.3px}
</style>
</head>
<body>
<main class="spread">
  <svg class="waves" viewBox="0 0 1140 443" aria-hidden="true">
    <path d="M330,314 C470,304 640,336 760,356 C880,374 1000,364 1140,340 L1140,352 C1000,378 880,390 760,372 C640,354 470,322 330,326Z" fill="var(--grey-band)"/>
    <path d="M0,340 C120,334 250,322 380,316" fill="none" stroke="var(--amber)" stroke-width="4"/>
    <path d="M0,395 C120,352 260,334 380,332 C560,330 650,364 760,380 C900,398 1030,378 1140,354 L1140,443 L760,443 L760,400 C650,388 560,348 380,346 C260,348 120,390 0,432Z" fill="var(--orange)"/>
  </svg>

  <section class="panel panel--about">
    <h2 class="section-title" style="left:78px;top:30px">
      <svg viewBox="0 0 140 50" aria-hidden="true"><path d="M8,10 C0,45 90,55 120,38" fill="none" stroke="var(--grey)" stroke-width="3"/></svg>
      About Us
    </h2>
    <p class="intro">At Pinecrest Treatment Center we believe strongly in providing the highest possible levels of care for you or your loved one. We have brought together some of the best and most experienced people in the industry to form our treatment team.</p>
    <div class="photo photo--yoga" role="img" aria-label="Woman meditating in a yoga pose on the beach at sunset"></div>
    <p class="side-text" style="left:186px;top:174px;width:168px">In addition, Pinecrest Treatment Center facilities are comprehensive and spacious, and offer comfortable accommodations that make the process of alcohol rehab or drug rehab less stressful. Pinecrest Treatment Center provides an environment where you or your loved one will find release from the enslavement of alcoholism or drug addiction.</p>
    <div class="brand"><span class="brand-dot"></span>Pinecrest</div>
  </section>

  <section class="panel panel--services">
    <h2 class="section-title" style="left:78px;top:20px">
      <svg viewBox="0 0 140 50" aria-hidden="true"><path d="M6,8 C0,50 110,58 130,32" fill="none" stroke="var(--grey)" stroke-width="3"/></svg>
      Our Services
    </h2>
    <h3 class="sub-title" style="left:20px;top:88px">Alcohol Rehab</h3>
    <div class="photo photo--group" role="img" aria-label="Man speaking to a seated support group"></div>
    <div class="side-text" style="left:160px;top:120px;width:200px">
      <p>Our dedicated staff are here to assist you or your loved one with recovery from the disease of alcoholism. We offer a comprehensive array of programs, starting with our residential detox program whenever necessary. Pinecrest Treatment Center also offers residential, partial hospitalization and intensive outpatient programs. Family support and trauma recovery are an integral component of our program as well, because we're focused on lifelong success for our clients.</p>
      <p>The alcohol rehab programs focus on building life skills that are necessary for successful, long-term healing. Weekly sessions consist of processing groups as well as substance abuse educational classes. We employ a skilled and experienced staff with a comprehensive and contemporary approach to recovery.</p>
    </div>
    <p class="call">Call <strong>555-210-4700</strong> Now</p>
  </section>

  <section class="panel panel--drug">
    <div class="photo photo--room" role="img" aria-label="Bright group therapy room with a circle of chairs"></div>
    <h3 class="sub-title" style="left:20px;top:88px">Drug Rehab</h3>
    <div class="photo photo--talk" role="img" aria-label="Young woman talking with a counselor on a sofa"></div>
    <div class="side-text side-text--tight" style="left:163px;top:120px;width:200px">
      <p>At Pinecrest Treatment Center, we offer a full array of affordable drug rehab programs that can take addicts from detox to inpatient or outpatient care and back home again. If you or your loved one requires detox from drugs, we take them through our residential detox program, and then after a thorough assessment help him or her determine the best treatment option. This may be residential treatment, partial hospitalization program or intensive outpatient care.</p>
      <p>If detox is not required we may admit someone directly into our residential inpatient program, or possibly suggest intensive outpatient services. One goal is to help each client to develop the life skills he or she needs to be successful after treatment. Our concerned and experienced staff are here to assist in each person through a comprehensive assessment and the entire recovery process, no matter the path chosen. At Pinecrest Treatment Center we are proud of our holistic treatment philosophy and the deep care and concern we feel for our clients.</p>
    </div>
    <p class="site">www.pinecrestcarehub.example</p>
  </section>
</main>
</body>
</html>
```